Gordon Pellbrook Consulting - Web Design Project

We need a web design for my new edgy consulting business specializing in innovation, technology and strategy.

It is our personal goal to turn each client into raving fans by helping them achieve their own business goals and aspirations through assisting them in raising their own innovation and marketing standards.

We provide our personalised and state-of-the-art services to our clients and boards who represent some of the world greatest innovative thinkers.
Updates

Here is some other information which may help shape your thinking.

I've had direct Involvement in the development of the following iPad, iPhone Applications and websites

FarbeyondOzlands.com (TerraLink platform) by Voyage Bureau
http://farbeyondozlands.example.au

Sail Verve by Bright Voyaging
https://apps.example-store.com/au/app/sail-verve/id100000001

uRedlandTR by Travel Territory Board
https://apps.example-store.com/au/app/uredlandtr/id100000002

Wexmoor Trips
http://www.wexmoortrips.example.au

Trek Mapper by Voyage Bureau
http://apps.example-store.com/au/app/trek-mapper/id100000003

Sunward by Sunward Travel Office
https://apps.example-store.com/au/app/sunward/id100000004

Upper Fernridge Valley Route by Visit Coastlands
https://apps.example-store.com/au/app/upper-fernridge-valley-route/id100000005

Wanderer Path by Travel Territory Board and Southern Plains Travel Council
https://apps.example-store.com/au/app/wanderers-path-grand-journey/id100000006

Gordon Pellbrook Consulting (GPC)
November 2012 – Present (8 months)Brisbane, Sydney, Canberra

Gordon’s consults to Small-to-Medium Enterprises (SME) and Government organisations on business strategy, technology strategy, risk mitigation, disruptive technology and innovation in the workplace.

Gordon’s consultancy mantra is that we cannot divorce economic life from cultural life particularly in an era when social capital may be as important as physical capital in business.

Reason: request from designers, I want to see their best efforts

Target Market(s)

35+

Industry/Entity Type

Business

Requirements
Must have
• Please use some of the personal image(s) contained in the zip files which can be downloaded from here

http://filedrop.example/k9Xq2Lm
http://filedrop.example/p4Rt7Vn
http://filedrop.example/z8Hw3Bc
Nice to have
• Black, Sleek design, maybe minimalist. Nice to have a Pixelle for the design. Nice to have it easily ported to Wordpress or be a modified Wordpress template. HTML 5, responsive design

```html
<!DOCTYPE html>
<html lang="en">
<head>
<meta charset="utf-8">
<title>Gordon Pellbrook Consulting</title>
<link rel="stylesheet" href="https://fonts.googleapis.com/css2?family=Oswald:wght@400;500&family=Roboto:wght@400&family=Yellowtail&display=swap">
<style>
:root{
  --orange:#f5842f;
  --orange-dark:#e0701c;
  --ink:#262626;
  --ink-2:#2d2d2d;
  --ink-3:#1f1f1f;
  --line:#3a3a3a;
  --text-light:#e6e6e6;
  --text-muted:#a3a3a3;
  --text-dim:#8a8a8a;
}
*{box-sizing:border-box;margin:0;padding:0}
html,body{width:836px;height:1200px;overflow:hidden;background:var(--ink)}
body{position:relative;font-family:'Roboto',sans-serif;color:var(--text-light)}
.abs{position:absolute}
.head{font-family:'Oswald',sans-serif;text-transform:uppercase}

/* header */
.site-header{left:0;top:0;width:836px;height:64px;background:var(--ink-2);border-bottom:2px solid var(--orange)}
.brand{left:99px;top:16px;display:flex;align-items:center;gap:9px}
.brand-square{width:62px;height:33px;background:var(--orange)}
.brand-name{color:var(--orange);font-family:'Oswald',sans-serif;font-weight:400;line-height:1}
.brand-name .n1{display:block;font-size:20px;letter-spacing:-.2px}
.brand-name .n2{display:block;font-size:9px;letter-spacing:6.2px;margin-top:3px}
.nav{top:29px;font-family:'Oswald',sans-serif;font-size:13px;color:#fff;text-transform:uppercase}
.nav.active{color:var(--orange)}

/* hero */
.hero{left:0;top:66px;width:836px;height:328px;background:radial-gradient(ellipse at 32% 45%,#9a9a9a 0%,#5b5b5b 35%,#2c2c2c 75%,#1b1b1b 100%)}
.hero-figure{left:100px;top:82px;width:300px;height:312px;background:linear-gradient(180deg,#8d8d8d 0%,#3a3a3a 60%,#1c1c1c 100%);border-radius:120px 120px 0 0}
.hero-title{left:430px;top:144px;font-family:'Yellowtail',cursive;font-size:40px;color:var(--orange)}
.hero-text{left:431px;top:206px;width:260px;font-size:12.5px;line-height:16.5px;color:#fff;letter-spacing:.3px}
.btn-orange{background:var(--orange);border:2px solid var(--orange-dark);color:#fff;font-family:'Oswald',sans-serif;text-transform:uppercase;text-align:center}
.hero-btn{left:432px;top:286px;width:120px;height:37px;font-size:21px;line-height:32px}
.pointer{left:410px;top:394px;width:0;height:0;border-left:8px solid transparent;border-right:8px solid transparent;border-top:7px solid #3b3b3b}

/* features */
.features{left:0;top:394px;width:836px;height:232px;background:var(--ink)}
.feature{top:430px;width:210px;text-align:center}
.feature-title{display:flex;align-items:center;justify-content:center;gap:8px}
.feature-icon{width:36px;height:36px;border-radius:50%;background:#fff;display:flex;align-items:center;justify-content:center}
.feature-title h2{font-family:'Oswald',sans-serif;font-weight:400;font-size:25px;color:var(--orange);text-transform:uppercase}
.feature p{margin-top:12px;font-size:10.5px;line-height:14px;color:var(--text-light)}
.pill{display:inline-block;margin-top:17px;width:88px;height:31px;border-radius:16px;background:linear-gradient(#4a4a4a,#2e2e2e);border:1px solid #1a1a1a;box-shadow:0 2px 3px rgba(0,0,0,.6);font-family:'Oswald',sans-serif;font-size:12.5px;line-height:29px;color:#fff;text-transform:uppercase}

/* welcome band */
.band{left:0;top:626px;width:836px;height:274px}
.welcome-title{left:94px;top:664px;font-family:'Oswald',sans-serif;font-weight:500;font-size:19px;color:#1a1a1a}
.welcome-text{left:94px;top:699px;width:300px;font-size:10.3px;line-height:15.5px;color:#1a1a1a}
.welcome-text p+p{margin-top:15.5px}
.divider{left:418px;top:674px;width:1px;height:168px;background:var(--orange-dark)}
.client-label{left:443px;top:672px;font-family:'Oswald',sans-serif;font-weight:500;font-size:13px;color:#1a1a1a}
.client-photo{left:443px;top:699px;width:62px;height:63px;border:3px solid #fff;background:linear-gradient(180deg,#c9a083,#6b4a36)}
.quote{left:531px;top:674px;width:212px;height:157px;background:var(--ink)}
.quote-tip{left:513px;top:692px;width:0;height:0;border-top:12px solid transparent;border-right:18px solid var(--ink)}
.quote-name{left:550px;top:694px;font-family:'Oswald',sans-serif;font-size:12.5px;color:#fff}
.quote-arrows{left:708px;top:682px;font-size:13px;color:#fff;letter-spacing:4px}
.quote-text{left:551px;top:716px;width:182px;font-size:9.3px;line-height:14.2px;color:var(--text-light)}

/* footer */
.footer-brand{left:94px;top:939px;display:flex;align-items:center;gap:8px}
.footer-brand .brand-square{width:53px;height:29px;background:#3a3a3a}
.footer-brand .brand-name{color:#7a7a7a}
.footer-brand .n1{font-size:18px}
.footer-brand .n2{font-size:8px;letter-spacing:5.6px}
.contact{left:94px;display:flex;gap:11px;font-size:10px;line-height:13.5px;color:var(--text-muted)}
.contact svg{flex:none;margin-top:1px}
.about{left:325px;top:940px;width:190px;font-size:10.2px;line-height:13.4px;color:var(--text-muted)}
.about p+p{margin-top:13px}
.signup{left:559px;top:940px;width:190px;font-size:10.2px;line-height:14px;color:var(--text-muted)}
.email{left:558px;top:1005px;width:184px;height:32px;border:1px solid #4a4a4a;background:#2b2b2b;font-size:11px;color:#9a9a9a;padding:9px 9px}
.subscribe{left:558px;top:1067px;width:88px;height:31px;font-size:18px;line-height:27px}
.to-top{left:780px;top:1068px;width:30px;height:30px;background:#1f1f1f;display:flex;align-items:center;justify-content:center}
.bottom-bar{left:0;top:1158px;width:836px;height:42px;background:var(--ink-3)}
.copyright{left:94px;top:1174px;font-size:9px;color:var(--text-dim)}
.follow{left:556px;top:1175px;font-size:8.5px;letter-spacing:.6px;color:var(--text-dim)}
.social{top:1168px;width:22px;height:21px;background:#3a3a3a}
</style>
</head>
<body>

<header class="abs site-header">
  <div class="abs brand">
    <span class="brand-square"></span>
    <span class="brand-name"><span class="n1">Gordon Pellbrook</span><span class="n2">CONSULTING</span></span>
  </div>
  <nav>
    <span class="abs nav active" style="left:428px">Home</span>
    <span class="abs nav" style="left:479px">About Us</span>
    <span class="abs nav" style="left:550px">Consulting</span>
    <span class="abs nav" style="left:630px">Clients</span>
    <span class="abs nav" style="left:691px">Contacts</span>
  </nav>
</header>

<section>
  <div class="abs hero" role="img" aria-label="Black and white photo of a blurred city street at night"></div>
  <div class="abs hero-figure" role="img" aria-label="Black and white portrait of the consultant in a dark suit and tie"></div>
  <div class="abs hero-title">Our personal goal...</div>
  <p class="abs hero-text">We will turn you into raving fans by helping you achieve your own business goals and aspirations</p>
  <div class="abs btn-orange hero-btn">Know More</div>
</section>

<section>
  <div class="abs features"></div>
  <div class="abs pointer"></div>

  <article class="abs feature" style="left:80px">
    <div class="feature-title">
      <span class="feature-icon"><svg width="20" height="20" viewBox="0 0 20 20" fill="none" stroke="#f5842f" stroke-width="1.4"><circle cx="10" cy="8" r="4.5"/><path d="M8 13h4M8.5 15.5h3M10 1v1.5M3 8H1.5M18.5 8H17M4.5 3l1 1M15.5 3l-1 1"/></svg></span>
      <h2>Innovation</h2>
    </div>
    <p>Aute iure reprehenderit in voluptate velit esse cillum dolore eu fugiat nulla pariatur. Lorem ipsum dolor sit amet, consetetur sadipscing elitr, sed diam.</p>
    <span class="pill">Know More</span>
  </article>

  <article class="abs feature" style="left:313px">
    <div class="feature-title">
      <span class="feature-icon"><svg width="22" height="20" viewBox="0 0 22 20" fill="#f5842f"><circle cx="7" cy="10" r="5"/><circle cx="7" cy="10" r="2" fill="#fff"/><circle cx="16" cy="10" r="3.6"/><circle cx="16" cy="10" r="1.3" fill="#fff"/></svg></span>
      <h2>Technology</h2>
    </div>
    <p>Aute iure reprehenderit in voluptate velit esse cillum dolore eu fugiat nulla pariatur. Lorem ipsum dolor sit amet, consetetur sadipscing elitr, sed diam.</p>
    <span class="pill">Know More</span>
  </article>

  <article class="abs feature" style="left:546px">
    <div class="feature-title">
      <span class="feature-icon"><svg width="20" height="20" viewBox="0 0 20 20" fill="#f5842f"><rect x="3" y="13" width="2.5" height="5"/><rect x="7" y="10" width="2.5" height="8"/><rect x="11" y="7" width="2.5" height="11"/><rect x="15" y="4" width="2.5" height="14"/><path d="M2 10l6-5 3 2 5-5" stroke="#f5842f" stroke-width="1.3" fill="none"/></svg></span>
      <h2>Strategy</h2>
    </div>
    <p>Aute iure reprehenderit in voluptate velit esse cillum dolore eu fugiat nulla pariatur. Lorem ipsum dolor sit amet, consetetur sadipscing elitr, sed diam.</p>
    <span class="pill">Know More</span>
  </article>
</section>

<section>
  <svg class="abs band" width="836" height="274" viewBox="0 0 836 274">
    <rect width="836" height="274" fill="#f5842f"/>
    <path d="M0 204 L232 273 L836 236 L836 274 L0 274 Z" fill="#262626"/>
  </svg>
  <h2 class="abs welcome-title">WELCOME</h2>
  <div class="abs welcome-text">
    <p>orem ipsum dolor sit amet, consectetur adipiscursus felis vel lacus cursus ullamcorper. Maecenas sed enim neque, quis rutrum arcu. Meceasa justo enim. Suspendisse suscipit malesuada magna, at sagittis augue varius ut.</p>
    <p>orem ipsum dolor sit amet, consectetur adipiscursus felis vel lacus cursus ullamcorper. Maecenas sed enim neque, quis rutrum arcu. Meceasa justo enim. Suspendisse suscipit.</p>
  </div>
  <div class="abs divider"></div>
  <h3 class="abs client-label">CLIENT SAYS</h3>
  <div class="abs client-photo" role="img" aria-label="Portrait photo of the client"></div>
  <div class="abs quote-tip"></div>
  <div class="abs quote"></div>
  <div class="abs quote-name">- Marcus Delaney</div>
  <div class="abs quote-arrows">&lsaquo;&rsaquo;</div>
  <p class="abs quote-text">orem ipsum dolor sit amet, consectetur adipiscursus felis vel lacus cursus ullamcorper. Maecenas sed enim neque, quis rutrum arcu. Meceasa justo enim. Suspendisse suscipit malesuada magna, at sagittis augue varius ut.</p>
</section>

<footer>
  <div class="abs footer-brand">
    <span class="brand-square"></span>
    <span class="brand-name"><span class="n1">Gordon Pellbrook</span><span class="n2">CONSULTING</span></span>
  </div>

  <div class="abs contact" style="top:990px">
    <svg width="12" height="11" viewBox="0 0 12 11" fill="#8a8a8a"><path d="M6 0L0 5.5h1.8V11h3V7.5h2.4V11h3V5.5H12z"/></svg>
    <span>418 Calloway Street, Dunmere,<br>Fairholt, QL 40127-2203</span>
  </div>
  <div class="abs contact" style="top:1031px">
    <svg width="12" height="13" viewBox="0 0 12 13" fill="#8a8a8a"><path d="M2 0l2.5 3-1.3 1.6c.8 1.8 2 3 3.6 3.8L8.4 7 11 9.5 9.3 12C4.5 11 1 7 0 2z"/></svg>
    <span>5550-142-7731</span>
  </div>
  <div class="abs contact" style="top:1057px">
    <svg width="12" height="11" viewBox="0 0 12 11" fill="#8a8a8a"><rect x="3" y="0" width="6" height="3"/><rect x="0" y="3.5" width="12" height="5"/><rect x="3" y="7" width="6" height="4" fill="#6a6a6a"/></svg>
    <span>5550-2261-4098</span>
  </div>
  <div class="abs contact" style="top:1084px">
    <svg width="12" height="9" viewBox="0 0 12 9" fill="#8a8a8a"><path d="M0 0h12v9H0z"/><path d="M0 0l6 5 6-5" stroke="#262626" fill="none"/></svg>
    <span>info@gordonpellbrook.example</span>
  </div>

  <div class="abs about">
    <p>Gordon’s consults to Small-to-Medium Enterprises (SME) and Government organisations on business strategy, technology strategy, risk mitigation, disruptive technology and innovation in the workplace.</p>
    <p>Gordon’s consultancy mantra is that we cannot divorce economic life from cultural life particularly in an era when social capital may be as important as physical capital in business.</p>
  </div>

  <p class="abs signup">Sign up to our Newsletter and receive occasional e-mail updates about new features and special offers from our comany.</p>
  <div class="abs email">Email address</div>
  <div class="abs btn-orange subscribe">Subscribe</div>
  <div class="abs to-top"><svg width="12" height="8" viewBox="0 0 12 8" fill="none" stroke="#ccc" stroke-width="1.5"><path d="M1 7l5-5 5 5"/></svg></div>

  <div class="abs bottom-bar"></div>
  <div class="abs copyright">Copyright © 2013.&nbsp; All Rights Reserved</div>
  <div class="abs follow">FOLLOW US ON</div>
  <span class="abs social" style="left:628px"></span>
  <span class="abs social" style="left:655px"></span>
</footer>

</body>
</html>
```